Pull Up Banners

Would like to have these pull up banner designs changed to a new modern theme. I have running a sales booth and want to re-design the banner designs. I have uploaded old banner design, I need phone number and website added onto bottom. Happy to consider images to attract people attention to increase sales and spark people interest walking past.

```html
<!DOCTYPE html>
<html lang="en">
<head>
<meta charset="utf-8">
<title>Brightdesk Pull Up Banners</title>
<link href="https://fonts.googleapis.com/css2?family=Exo+2:wght@600;700;800&family=Ubuntu:wght@400;700&display=swap" rel="stylesheet">
<style>
  :root {
    --stage: #3f3f3f;
    --white: #ffffff;
    --orange: #e85d0f;
    --orange-bright: #f26a1b;
    --ink: #1a1a1a;
    --dark-edge: #2a0e07;
    --ember: #a8380f;
  }
  * { margin: 0; padding: 0; box-sizing: border-box; }
  html, body { width: 1200px; height: 2594px; overflow: hidden; }
  body { background: var(--stage); position: relative; font-family: "Exo 2", sans-serif; }

  .banner {
    position: absolute; top: 622px; width: 540px; height: 1350px;
    background: var(--white); overflow: hidden;
  }
  .banner--phone { left: 40px; }
  .banner--managed { left: 620px; }

  .banner__art { position: absolute; inset: 0; width: 540px; height: 1350px; }

  .brand {
    position: absolute; top: 118px; left: 0; width: 100%;
    display: flex; align-items: center; justify-content: center; gap: 14px;
  }
  .brand__dot { width: 40px; height: 40px; border-radius: 50%; background: var(--orange); }
  .brand__name {
    font-family: "Exo 2", sans-serif; font-weight: 800; font-size: 58px;
    color: var(--ink); letter-spacing: 1px;
  }

  .headline {
    position: absolute; top: 278px; left: 20px; width: 500px; text-align: center;
    font-weight: 800; text-transform: uppercase; line-height: 1.05;
  }
  .headline__main { display: block; font-size: 50px; color: var(--orange); }
  .headline__sub { display: block; font-size: 36px; color: var(--ink); margin-top: 10px; }
  .headline__sub .accent { color: var(--orange); }
  .banner--managed .headline__main { font-size: 50px; }
  .banner--managed .headline__sub { font-size: 52px; margin-top: 8px; }

  .services { position: absolute; left: 0; top: 0; width: 100%; list-style: none; }
  .service {
    position: absolute; left: 183px; width: 345px;
    transform: translateY(-50%);
    font-weight: 700; font-size: 33px; line-height: 1.28; color: var(--white);
    text-shadow: 0 2px 4px rgba(0,0,0,0.45);
  }
  .banner--managed .service { font-size: 31px; }

  .web {
    position: absolute; left: 0; bottom: 0; width: 100%; height: 94px;
    display: flex; align-items: center; justify-content: center;
    font-family: "Ubuntu", sans-serif; font-size: 30px; color: var(--orange);
  }
  .web strong { font-weight: 700; }
</style>
</head>
<body>

<section class="banner banner--phone">
  <svg class="banner__art" viewBox="0 0 540 1350" aria-hidden="false">
    <defs>
      <radialGradient id="glowA" cx="0.62" cy="0.42" r="0.75">
        <stop offset="0" stop-color="#d9571b"/>
        <stop offset="0.45" stop-color="#8f2e0e"/>
        <stop offset="1" stop-color="#2a0e07"/>
      </radialGradient>
    </defs>
    <rect x="0" y="360" width="540" height="896" fill="url(#glowA)" role="img" aria-label="Glowing orange network-of-dots backdrop"/>
    <rect x="47" y="330" width="120" height="882" rx="60" fill="var(--orange)"/>
    <path d="M0,395 C-5,280 130,245 290,248 C430,250 520,290 540,340 L540,420 C520,510 420,540 300,530 C160,520 40,480 0,440 Z" fill="var(--orange)"/>
    <path d="M14,400 C10,300 130,258 285,258 C420,258 510,300 518,345 C525,430 430,505 300,500 C170,495 40,460 14,400 Z" fill="var(--white)"/>
    <g fill="none" stroke="var(--white)" stroke-width="3">
      <circle cx="107" cy="630" r="42"/>
      <circle cx="107" cy="802" r="42"/>
      <circle cx="107" cy="972" r="42"/>
      <circle cx="107" cy="1146" r="42"/>
    </g>
    <g fill="var(--white)" stroke="var(--white)" stroke-linecap="round">
      <!-- phone -->
      <path d="M94,612 l8,-4 l7,13 l-6,5 c3,7 7,12 13,15 l5,-6 l13,8 l-4,8 c-18,3 -40,-20 -36,-39 z" stroke="none"/>
      <path d="M115,612 a12,12 0 0 1 12,12 M117,603 a21,21 0 0 1 19,19" fill="none" stroke-width="3"/>
      <!-- chat -->
      <path d="M84,786 h46 a6,6 0 0 1 6,6 v22 a6,6 0 0 1 -6,6 h-28 l-10,9 v-9 h-8 a6,6 0 0 1 -6,-6 v-22 a6,6 0 0 1 6,-6 z" stroke="none"/>
      <path d="M90,796 h34 M90,803 h34 M90,810 h34" stroke="var(--orange)" stroke-width="3" fill="none"/>
      <!-- people -->
      <circle cx="107" cy="960" r="8" stroke="none"/>
      <circle cx="88" cy="964" r="6" stroke="none"/>
      <circle cx="126" cy="964" r="6" stroke="none"/>
      <path d="M93,988 a14,14 0 0 1 28,0 z M76,986 a12,12 0 0 1 20,-8 l-4,8 z M138,986 a12,12 0 0 0 -20,-8 l4,8 z" stroke="none"/>
      <!-- wifi -->
      <path d="M83,1137 a34,34 0 0 1 48,0 M90,1145 a24,24 0 0 1 34,0 M97,1153 a14,14 0 0 1 20,0" fill="none" stroke-width="5"/>
      <circle cx="107" cy="1162" r="4.5" stroke="none"/>
    </g>
  </svg>

  <div class="brand"><span class="brand__dot"></span><span class="brand__name">BRIGHTDESK</span></div>

  <h1 class="headline">
    <span class="headline__main">Cloud Phone</span>
    <span class="headline__sub"><span class="accent">System</span> &amp; Internet</span>
  </h1>

  <ul class="services">
    <li class="service" style="top:630px">VoIP &amp; Phone<br>Systems</li>
    <li class="service" style="top:802px; left:188px">SMS Gateway</li>
    <li class="service" style="top:972px; left:188px">Teamlink<br>Calling</li>
    <li class="service" style="top:1146px; left:196px">NetGrid, Fibre &amp; 4G<br>Internet</li>
  </ul>

  <p class="web">www.<strong>brightdesktech</strong>.com.au</p>
</section>

<section class="banner banner--managed">
  <svg class="banner__art" viewBox="0 0 540 1350">
    <defs>
      <radialGradient id="glowB" cx="0.62" cy="0.45" r="0.75">
        <stop offset="0" stop-color="#d9571b"/>
        <stop offset="0.45" stop-color="#8f2e0e"/>
        <stop offset="1" stop-color="#2a0e07"/>
      </radialGradient>
    </defs>
    <rect x="0" y="360" width="540" height="896" fill="url(#glowB)" role="img" aria-label="Glowing orange network-of-dots backdrop"/>
    <rect x="47" y="330" width="120" height="882" rx="60" fill="var(--orange)"/>
    <path d="M0,395 C-5,280 130,245 290,248 C430,250 520,290 540,340 L540,420 C520,510 420,540 300,530 C160,520 40,480 0,440 Z" fill="var(--orange)"/>
    <path d="M14,400 C10,300 130,258 285,258 C420,258 510,300 518,345 C525,430 430,505 300,500 C170,495 40,460 14,400 Z" fill="var(--white)"/>
    <g fill="none" stroke="var(--white)" stroke-width="3">
      <circle cx="107" cy="630" r="40"/>
      <circle cx="107" cy="762" r="40"/>
      <circle cx="107" cy="894" r="40"/>
      <circle cx="107" cy="1026" r="40"/>
      <circle cx="107" cy="1158" r="40"/>
    </g>
    <g fill="none" stroke="var(--white)" stroke-width="3.5" stroke-linecap="round" stroke-linejoin="round">
      <!-- monitor -->
      <rect x="86" y="613" width="42" height="28" rx="3"/>
      <path d="M100,648 h14 M107,641 v7"/>
      <!-- shield -->
      <path d="M107,740 l20,8 c0,18 -8,30 -20,36 c-12,-6 -20,-18 -20,-36 z"/>
      <rect x="101" y="762" width="12" height="9" rx="1.5"/>
      <path d="M103,762 v-4 a4,4 0 0 1 8,0 v4"/>
      <!-- cloud -->
      <path d="M92,900 a10,10 0 0 1 2,-20 a14,14 0 0 1 26,-2 a10,10 0 0 1 2,22 z"/>
      <path d="M100,900 v10 M114,900 v10 M107,900 v14"/>
      <!-- envelope -->
      <rect x="85" y="1012" width="44" height="30" rx="3"/>
      <path d="M86,1014 l21,16 l21,-16"/>
      <!-- globe -->
      <circle cx="107" cy="1158" r="20"/>
      <ellipse cx="107" cy="1158" rx="9" ry="20"/>
      <path d="M87,1158 h40 M91,1147 h32 M91,1169 h32"/>
    </g>
  </svg>

  <div class="brand"><span class="brand__dot"></span><span class="brand__name">BRIGHTDESK</span></div>

  <h1 class="headline">
    <span class="headline__main">Managed I.T</span>
    <span class="headline__sub">Services</span>
  </h1>

  <ul class="services">
    <li class="service" style="top:630px">Managed I.T<br>Support</li>
    <li class="service" style="top:762px">Cybersecurity<br>Solutions</li>
    <li class="service" style="top:894px">Cloud Servers &amp;<br>Backups</li>
    <li class="service" style="top:1026px">Cloudsuite Email<br>Packs</li>
    <li class="service" style="top:1158px">Domains &amp;<br>Websites</li>
  </ul>

  <p class="web">www.<strong>brightdesktech</strong>.com.au</p>
</section>

</body>
</html>
```